Web Design Project

We need web design for a new baby products (nursery furniture) business in Australia.

The logo is already done, and I would like to reflect a similar theme throughout the website:
* Clean, white background.
* Use of lime green, purple and orange.
* Similar font to logo for headings
* FUNKY, FASHIONABLE, QUALITY feeling of website.

The main concept is to be attractive to discerning mums who are buying big items like a cot or chest of drawers. These are expensive items and will be considered the most important purchases for a newborn, so the website has to be enticing!!!
Updates

Hello,

Thank you for your submissions. I have received a few questions regarding the font and the coding of this website.

The job I am seeking is for design for an E-commerce store. The font was done by another craft hive designer, so I do not know what type of font I am sorry.

I was hoping to have more designs by now, so please send them soon, this project is guaranteed!

I also ask you to read the brief properly please. The name of the business is Cradle Lane, as the logo says. The use of design that I have mentioned has only been demonstrated in a couple of designs submitted to me.

I look forward to seeing your work soon!

Kind Regards
Marla

Target Market(s)

Young mothers aged 25-45

Industry/Entity Type

Business

Requirements
Must have
• Must be funky, bright, energetic, attractive visually.
Nice to have
• I like the idea of some floral / design work in faded lime green, purple on some of the edges of different pages. Maybe islamic design? But has to be very fashionable.
Should not have
• Should not have any traditional ideas of baby websites.

ie- no stork, nappy images, teddybears etc.

```html
<!DOCTYPE html>
<html lang="en">
<head>
<meta charset="utf-8">
<title>Cradle Lane – Home</title>
<link rel="stylesheet" href="https://fonts.googleapis.com/css2?family=Comfortaa:wght@400;700&family=Open+Sans:wght@400;600;700&family=Arimo:wght@400;700&family=Tinos:wght@400;700&display=swap">
<style>
:root{
  --lime:#8cc63f;
  --lime-dark:#7ab51d;
  --purple:#a66bb4;
  --purple-dark:#8e3f9b;
  --plum:#8b1d8f;
  --orange:#f08a12;
  --orange-light:#f7a83a;
  --grey:#666;
  --grey-light:#e4e4e4;
  --green-card:#74bd7a;
  --orange-card:#f2a500;
  --white:#fff;
}
*{box-sizing:border-box;margin:0;padding:0}
html,body{width:1075px;height:1200px;overflow:hidden;background:var(--white)}
body{position:relative;font-family:"Open Sans",sans-serif;color:var(--grey)}
.abs{position:absolute}
.pattern{position:absolute;background:linear-gradient(135deg,#1f2e86,#2b3f9c 40%,#3d7a3a 70%,#1f2e86)}
.pattern-left{left:0;top:0;width:106px;height:1200px}
.pattern-right{left:969px;top:0;width:106px;height:1200px}
.pattern-bottom{left:106px;top:1160px;width:863px;height:40px}

.topbar{left:106px;top:0;width:863px;height:31px;background:var(--lime);border-radius:0 0 50% 50% / 0 0 60% 60%;
  font-family:"Comfortaa",sans-serif;font-size:10px;color:#d8f0a8}
.topbar a{position:absolute;top:3px;color:inherit;text-decoration:none;white-space:nowrap}
.cart-icon{position:absolute;left:700px;top:3px}

.tagline{left:118px;top:52px;width:278px;text-align:center;font-family:"Comfortaa",sans-serif;font-size:13px;color:#777;line-height:15px}
.tagline strong{display:block;margin-top:8px;font-family:"Open Sans",sans-serif;font-weight:400;font-size:15px;color:var(--plum)}
.brand{left:400px;top:52px;display:flex;align-items:center;gap:10px}
.brand-mark{width:54px;height:54px;border-radius:50%;background:var(--lime)}
.brand-name{font-family:"Comfortaa",sans-serif;font-weight:700;font-size:34px;color:var(--purple-dark);line-height:36px}
.contact{left:712px;top:44px;width:252px;font-family:"Comfortaa",sans-serif;color:#666}
.contact h2{font-weight:400;font-size:16px;letter-spacing:1px;text-align:center;margin-bottom:8px}
.contact p{font-size:12.5px;display:flex;align-items:center;gap:6px;margin-bottom:7px;white-space:nowrap}

.nav{left:116px;top:133px;width:844px;height:39px;display:flex;gap:3px}
.nav a{flex:1;background:linear-gradient(#f9a94a,var(--orange) 55%,#e07400);border-radius:6px;color:#fff;
  font-family:"Arimo",sans-serif;font-weight:700;font-size:15px;letter-spacing:.5px;display:flex;align-items:center;justify-content:center;text-decoration:none}
.nav a.contact-btn{margin-left:6px}

.panel-head{background:var(--purple);color:#fff;font-family:"Comfortaa",sans-serif;text-align:center;font-weight:400}
.categories{left:116px;top:191px;width:152px;height:272px;border:1px solid #ccc}
.categories .panel-head{height:27px;font-size:15px;line-height:27px;letter-spacing:.5px}
.categories ul{list-style:none;padding:7px 0 0 8px;font-family:"Comfortaa",sans-serif;font-size:10px;line-height:14.3px;color:#777;letter-spacing:.3px;white-space:nowrap}
.categories .hl{color:var(--orange)}
.categories .sub{padding-left:24px}

.featured{left:118px;top:475px;width:152px;height:336px;border:1px solid #ccc;border-top:none;text-align:center}
.featured .panel-head{height:21px;font-size:15px;line-height:21px;letter-spacing:1px;margin:0 -1px}
.product{position:absolute;left:0;width:100%;font-size:9px;line-height:11px;letter-spacing:.4px;color:#555}
.product .shot{margin:0 auto 15px}
.product .price{margin-top:8px}

.loyalty{left:124px;top:824px;width:154px;height:140px}

.welcome{left:295px;top:192px;font-family:"Comfortaa",sans-serif;color:var(--orange)}
.welcome h1{font-size:15px;font-weight:700;letter-spacing:1px}
.welcome p{font-size:12px;margin-top:13px}
.slider{left:290px;top:258px;width:493px;height:235px;background:var(--grey-light)}
.slide{position:absolute;left:47px;top:8px;width:405px;height:178px;background:#fff}
.slide-photo{position:absolute;left:9px;top:6px;width:203px;height:166px;background:linear-gradient(135deg,#d9c7e0,#efe6ea 50%,#c9b7c8)}
.slide-copy{position:absolute;right:12px;top:16px;width:170px;text-align:right;font-family:"Comfortaa",sans-serif;font-size:14px;line-height:16px;color:#3aa43a}
.slide-copy p+p{margin-top:40px}
.arrow{position:absolute;top:128px}
.thumbs{position:absolute;left:132px;top:195px;display:flex;gap:7px}
.thumbs span{width:46px;height:40px;display:block}

.copy{left:290px;top:501px;width:470px;font-size:12.4px;line-height:13.6px;color:#555;letter-spacing:.4px}
.copy p+p{margin-top:16px}

.testimonials{left:292px;top:776px;width:484px;height:201px;background:var(--lime);box-shadow:2px 2px 3px rgba(0,0,0,.3)}
.testimonials h2{text-align:center;color:#fff;font-family:"Arimo",sans-serif;font-size:21px;font-weight:700;letter-spacing:.5px;margin-top:3px}
.t-photo{position:absolute;left:18px;width:88px;height:72px;background:#fff;border:1px solid #ccc;font-size:6px;color:#bbb;text-align:center;padding-top:26px;line-height:7px}
.t-card{position:absolute;left:133px;width:343px;height:79px;color:#fff;font-family:"Arimo",sans-serif;padding:4px 0 0 1px}
.t-card b{font-weight:400;font-size:12px;display:block;margin-bottom:7px}
.t-card i{font-style:normal;font-size:6.8px;line-height:9px;display:block;margin-top:8px}

.search{left:802px;top:188px;width:156px;height:49px;border:1px solid #ddd}
.search .panel-head{height:22px;font-size:13px;line-height:22px;letter-spacing:1px}
.mailing{left:805px;top:253px;width:152px;height:122px;border:1px solid #ddd;font-size:10px}
.mailing .panel-head{height:38px;font-size:13px;line-height:16px;padding-top:4px}
.mailing label{display:flex;align-items:center;justify-content:space-between;padding:0 8px 0 3px;margin-top:7px}
.mailing input,.search input{border:1px solid #aaa;height:13px;width:86px}
.submit{display:block;margin:10px auto 0;width:48px;height:16px;background:var(--orange);color:#fff;border-radius:3px;font-family:"Comfortaa",sans-serif;font-size:9px;text-align:center;line-height:16px}
.map{left:805px;top:385px;width:153px;height:164px}
.map .panel-head{height:38px;font-size:13px;line-height:16px;padding-top:4px}
.map-area{height:126px;background:linear-gradient(160deg,#c6dcef,#e6eef2 45%,#a9c9e8);position:relative}
.map-tabs{position:absolute;right:3px;top:5px;display:flex;font-size:9px;font-family:"Arimo",sans-serif;background:#fff;border:1px solid #999}
.map-tabs span{padding:1px 5px}
.map-tabs span:first-child{font-weight:700;border-right:1px solid #999}
.hours{left:800px;top:571px;width:155px;height:182px;border-left:2px solid var(--purple);border-right:2px solid var(--purple);text-align:center;font-size:12.6px;color:#555;padding-top:1px}
.hours h3{font-size:12.6px;font-weight:700;margin-bottom:21px}
.hours b{display:block;font-weight:700}
.hours span{display:block;margin:4px 0 8px}
.faq{left:810px;top:781px;width:157px;height:81px;background:var(--lime-dark);border-radius:6px 0 0 0;color:#fff;padding:2px 0 0 14px;overflow:hidden}
.faq strong{font-family:"Comfortaa",sans-serif;font-weight:700;font-size:36px;display:block;line-height:46px}
.faq span{font-size:11px;line-height:12px;display:block;width:120px;margin-top:5px;color:#eafad0}
.social-badge{left:810px;top:883px;width:153px;height:69px;background:linear-gradient(#f2f4f8,#dfe4ee);text-align:center;font-size:11px;color:#333;padding-top:10px}
.social-badge .like{display:inline-block;border:1px solid #9aa;background:#fff;padding:1px 6px;font-size:10px}
.social-badge b{display:block;color:#2c4a8c;font-size:14px;margin:3px 0 2px}
.social-badge em{font-style:normal;color:#d6251c;font-size:9px;font-weight:700}

.rule{left:106px;top:996px;width:863px;height:15px;background:var(--orange)}
.footer{left:106px;top:1011px;width:863px;height:149px;background:var(--purple);border:3px solid #8a59a0;border-top:none;font-family:"Tinos",serif;font-size:11.5px;color:#fff}
.f-col{position:absolute;top:3px;line-height:15px;white-space:nowrap}
.f-col h4{font-size:11.5px;text-align:center;margin-bottom:1px}
.f-col ul{list-style:none}
.f-col li::before{content:"• "}
.social{position:absolute;left:628px;top:8px;text-align:center;font-family:"Comfortaa",sans-serif;font-style:italic;color:var(--orange-light);font-size:16px;line-height:20px;width:136px}
.social-icons{position:absolute;left:604px;top:60px;display:flex;gap:10px}
.social-icons span{width:22px;height:22px;border-radius:50%;background:#fff;opacity:.9}
.copyright{position:absolute;left:0;width:100%;top:130px;text-align:center;font-family:"Open Sans",sans-serif;font-size:10px}
</style>
</head>
<body>

<div class="pattern pattern-left" role="img" aria-label="Decorative Islamic floral tile border in navy, lime and yellow"></div>
<div class="pattern pattern-right" role="img" aria-label="Decorative Islamic floral tile border in navy, lime and yellow"></div>
<div class="pattern pattern-bottom" role="img" aria-label="Decorative Islamic floral tile border"></div>

<header>
  <nav class="abs topbar">
    <a style="left:36px">Sign In</a>
    <a style="left:98px">Your Account</a>
    <a style="left:194px">Customer Service</a>
    <a style="left:318px">Contact Us</a>
    <svg class="cart-icon" width="22" height="16" viewBox="0 0 22 16"><path d="M1 2h4l3 9h10l2-6H7" fill="none" stroke="var(--orange)" stroke-width="2"/><circle cx="9" cy="14" r="1.6" fill="var(--orange)"/><circle cx="16" cy="14" r="1.6" fill="var(--orange)"/></svg>
    <a style="left:726px">Your Shopping Cart: $0.00</a>
  </nav>

  <div class="abs tagline">Aliquam eleifend lacus ac tellus volutpat porttitor.<strong>Tagline/Slogan</strong></div>

  <div class="abs brand"><span class="brand-mark"></span><span class="brand-name">Cradle Lane</span></div>

  <div class="abs contact">
    <h2>CONTACT US</h2>
    <p><svg width="16" height="14" viewBox="0 0 16 14"><path d="M2 4c0-2 12-2 12 0v2h-3V5H5v1H2zM4 7h8l2 6H2z" fill="var(--orange-light)"/></svg>Phone: &nbsp;1-800-555-0142</p>
    <p><svg width="18" height="13" viewBox="0 0 18 13"><rect width="18" height="13" rx="1" fill="var(--orange-light)"/><path d="M0 1l9 6 9-6" fill="none" stroke="#fff" stroke-width="1.3"/></svg>Email: &nbsp;&nbsp;&nbsp;&nbsp;hello@cradlelane.au</p>
  </div>

  <nav class="abs nav">
    <a href="#">HOME</a><a href="#"></a><a href="#"></a><a href="#"></a><a href="#"></a><a href="#"></a><a href="#"></a><a href="#" class="contact-btn">CONTACT</a>
  </nav>
</header>

<aside>
  <section class="abs categories">
    <h2 class="panel-head">Categories</h2>
    <ul>
      <li class="hl">Baby Cribs</li>
      <li class="hl sub">By Brand</li>
      <li class="hl sub">By Style</li>
      <li class="hl">These are roll-overs</li>
      <li>Baby Bassinets</li><li>High Chairs</li><li>Baby Travel Cot</li><li>Baby Tables</li>
      <li>Baby Accessories</li><li>Baby Rugs</li><li>Decals/Room Stencils</li><li>Baby Bunting</li>
      <li>Mattresses</li><li>Baby Lamps</li><li>Baby Decor</li><li>Specials!</li>
    </ul>
  </section>

  <section class="abs featured">
    <h2 class="panel-head">FEATURED</h2>
    <div class="product" style="top:38px">
      <div class="shot" role="img" aria-label="Carved wooden room divider screen" style="width:110px;height:92px;background:linear-gradient(#eee3d4,#d9c6ae)"></div>
      Product Rotator with<br>Featured Products<div class="price">$00.00</div>
    </div>
    <div class="product" style="top:192px">
      <div class="shot" role="img" aria-label="Cream lace-draped bassinet" style="width:104px;height:88px;background:linear-gradient(#7d8a55,#e9e2cf 60%,#d5ccb4)"></div>
      Product Rotator with<br>Featured Products<div class="price">$00.00</div>
    </div>
  </section>

  <div class="abs loyalty">
    <div role="img" aria-label="Floral mandala badge frame" style="position:absolute;inset:0;border-radius:50%;background:radial-gradient(circle,#f7a21b 55%,#6b4a9e 58%,#4e9a3c 75%,#d4e04b)"></div>
    <div style="position:absolute;left:0;right:0;top:26px;text-align:center;font-family:Comfortaa,sans-serif;font-weight:700;font-size:16px;line-height:20px;color:var(--plum)">Join Our<br>Loyalty<br>Program</div>
    <div style="position:absolute;left:0;right:0;top:96px;height:18px;background:var(--purple);border:1px solid #fff;color:#fff;font-size:9px;font-weight:700;text-align:center;line-height:16px">Read About The Rewards!</div>
  </div>
</aside>

<main>
  <div class="abs welcome">
    <h1>WELCOME TO CRADLE LANE</h1>
    <p>Your only choice for your “precious” baby’s needs.</p>
  </div>

  <section class="abs slider">
    <div class="slide">
      <div class="slide-photo" role="img" aria-label="Pastel mosaic-painted nursery furniture set"></div>
      <div class="slide-copy"><p>Aliquam eleifend lacus ac tellus volutpat porttitor.</p><p>Suspen imperdiet tortor ut tortor bibendum.</p></div>
    </div>
    <svg class="arrow" style="left:8px" width="24" height="24" viewBox="0 0 24 24"><circle cx="12" cy="12" r="12" fill="var(--orange)"/><path d="M15 6l-7 6 7 6z" fill="#fff"/></svg>
    <svg class="arrow" style="left:463px" width="24" height="24" viewBox="0 0 24 24"><circle cx="12" cy="12" r="12" fill="var(--orange)"/><path d="M9 6l7 6-7 6z" fill="#fff"/></svg>
    <div class="thumbs">
      <span role="img" aria-label="Thumbnail of mosaic nursery set" style="background:#d5c8d8"></span>
      <span role="img" aria-label="Thumbnail of white bassinet in garden" style="background:#6f8a4a"></span>
      <span role="img" aria-label="Thumbnail of purple nursery room" style="background:#8a6a9a"></span>
      <span role="img" aria-label="Thumbnail of lace bassinet" style="background:#c9c1a5"></span>
    </div>
  </section>

  <div class="abs copy">
    <p>Cras euismod, sapien ut accumsan feugiat, mauris erat auctor metus, sed pellentesque massa tellus non enim. Aliquam commodo, risus sed posuere eleifend, odio nisi rhoncus nisl, vitae pharetra sem arcu non dui. Pellentesque sodales odio nec justo bibendum vitae porttitor metus luctus. Nulla volutpat, arcu in convallis imperdiet, arcu velit auctor purus, a rutrum nunc neque at elit. Cras euismod, sapien ut accumsan feugiat, mauris erat auctor metus, sed pellentesque massa tellus non enim.</p>
    <p>Cras euismod, sapien ut accumsan feugiat, mauris erat auctor metus, sed pellentesque massa tellus non enim. Aliquam commodo, risus sed posuere eleifend, odio nisi rhoncus nisl, vitae pharetra sem arcu non dui. Pellentesque sodales odio nec justo bibendum vitae porttitor metus luctus. Nulla volutpat, arcu in convallis imperdiet, arcu velit auctor purus, a rutrum nunc neque at elit. Cras euismod, sapien ut accumsan feugiat, mauris erat auctor metus, sed pellentesque massa tellus non enim.</p>
  </div>

  <section class="abs testimonials">
    <h2>Vestibulum velit orci</h2>
    <div class="t-photo" style="top:39px">Click here to add photo<br>or<br>Drag photo here</div>
    <div class="t-card" style="top:32px;background:var(--green-card)"><b>Rowan</b><b>Job Title</b><i>“Nulla vestibulum eleifend nulla. Suspendisse potenti. Aliquam turpis nisi, venenatis non, accumsan nec, imperdiet laoreet, lacus.”</i></div>
    <div class="t-photo" style="top:123px">Click here to add photo<br>or<br>Drag photo here</div>
    <div class="t-card" style="top:115px;background:var(--orange-card)"><b>Rowan</b><b>Job Title</b><i>“Pellentesque tincidunt, dolor eu dignissim mollis, justo sapien iaculis pede, vel tincidunt lacus nisl sit amet metus.”</i></div>
  </section>
</main>

<aside>
  <section class="abs search">
    <h2 class="panel-head">Search Our Site</h2>
    <div style="display:flex;align-items:center;gap:10px;padding:4px 6px">
      <svg width="18" height="18" viewBox="0 0 18 18"><circle cx="11" cy="7" r="5.5" fill="#dfe8f5" stroke="#666" stroke-width="1.5"/><path d="M7 11l-5 5" stroke="#666" stroke-width="2.5"/></svg>
      <input type="text" style="width:104px" aria-label="Search">
    </div>
  </section>

  <section class="abs mailing">
    <h2 class="panel-head">Join Our<br>Mailing List</h2>
    <label style="margin-top:10px">Name: <input type="text"></label>
    <label>Email: <input type="text"></label>
    <span class="submit">Submit</span>
  </section>

  <section class="abs map">
    <h2 class="panel-head">Store:<br>Map &amp; Directions</h2>
    <div class="map-area" role="img" aria-label="World map showing store location">
      <div class="map-tabs"><span>Map</span><span>Satellite</span></div>
    </div>
  </section>

  <section class="abs hours">
    <h3>Store Hours:</h3>
    <b>Monday-Friday</b><span>9:00am-6:00pm</span>
    <b>Saturday</b><span>9:00am- 8:00pm</span>
    <b>Sunday</b><b><i>Closed</i></b>
  </section>

  <div class="abs faq"><strong>faq’s</strong><span>frequently asked<br>questions</span></div>

  <div class="abs social-badge"><span class="like">Like</span><b>Like us on Friendnet</b><em>and get exclusive offers!</em></div>
</aside>

<div class="abs rule"></div>
<footer class="abs footer">
  <div class="f-col" style="left:44px"><h4>Company</h4><ul><li>About Us</li><li>As Seen In</li><li>Media Inquiry</li><li>For Affiliates</li><li>Safety Statement</li><li>Contact Us</li></ul></div>
  <div class="f-col" style="left:195px"><h4>Store-Online</h4><ul><li>Sign In</li><li>Register</li><li>Shipping Information</li><li>Return Policy</li><li>Privacy Policy</li><li>Terms &amp; Conditions</li></ul></div>
  <div class="f-col" style="left:335px;top:7px"><ul><li>Your Account</li><li>Shopping Cart</li><li>Account History</li><li style="margin-top:10px">Site Map</li></ul></div>
  <div class="f-col" style="left:475px"><h4 style="color:var(--lime);text-align:left;padding-left:12px">Loyalty Program</h4><ul><li>Register for Program</li><li>Sign In</li><li>Check your account</li><li>Refer a Friend</li></ul></div>
  <div class="social">We Are Social<br>Follow us:</div>
  <div class="social-icons"><span></span><span></span><span></span><span></span><span></span></div>
  <svg style="position:absolute;left:695px;top:97px" width="40" height="36" viewBox="0 0 40 36"><circle cx="6" cy="30" r="5" fill="var(--orange)"/><path d="M2 16a18 18 0 0 1 18 18M2 4a30 30 0 0 1 30 30" fill="none" stroke="var(--orange)" stroke-width="5"/></svg>
  <div class="copyright">© 2012 Cradle Lane, Inc. All Rights Reserved.</div>
</footer>

</body>
</html>
```